Corvalinks LLC vision casting home page design

A website for our business, Corvalinks LLC. We empower leadership with insights and data to help them make excellent decisions for their communities. Our initial product is a SMS product that allows people to take survey via text using our application that requires no download, helping them share their voice and feel a greater sense of belonging with their community. We would like to see designs that use the color purple. The final design should communicate wisdom and should appeal to the Pope as a one-day asset to the Vatican and it's operations.

Designers,

In the brief, I have requested 3 pages to be designed. The designs submitted I am thinking could be good for page 2 or 3 getting at our first product, but for the main page I am requesting more designs that sell the Corvalink's vision.

The vision is for Corvalinks to one day become a data organization. The data we will collect captures each individual church attender and participant, creates a profile for them based on the sin-to-saint spectrum model, and provides support to move individuals toward sanctification. As a one day auxiliary arm of the church, Corvalinks is positioned to become an asset to church operations by keeping grounded in our founding pillars, trusting in the movements of the Holy Spirit, and staying obedient to the office of the magisterium.

I am seeking more designs that cast this vision in a compelling way for the Corvalink's home page.
Updates

Our A2P (application to person) messaging service is very new and will likely take some convincing for churches to adopt. I would like the web site to be a sales page of sorts that really sells this concept.

I uploaded a new element to the project. I would love to see the uploaded sales pitch worked into the designs

Target Market(s)

Should appeal mostly to local priests and their leadership teams

Industry/Entity Type

Religious

Number of Pages Required

3 page

Font styles to use
Other font styles liked:
• Open to fonts

Requirements
Must have
• The uploaded sales pitch
Nice to have
• Stages of Belonging

```html
<!DOCTYPE html>
<html lang="en">
<head>
<meta charset="utf-8">
<title>Corvalinks LLC — Home</title>
<link href="https://fonts.googleapis.com/css2?family=League+Spartan:wght@300;400;500;600;700&family=Great+Vibes&display=swap" rel="stylesheet">
<style>
:root{
  --purple-deep:#4a1e6b;
  --purple:#5b2a83;
  --purple-mid:#6c3596;
  --lilac:#c9a8e2;
  --lilac-soft:#e6d6f2;
  --ink:#2b2233;
  --text:#4a4452;
  --white:#ffffff;
  --footer:#231f22;
  --footer-text:#c9c3cf;
}
*{box-sizing:border-box;margin:0;padding:0}
html,body{width:1200px;height:3713px;overflow:hidden}
body{font-family:"League Spartan",sans-serif;color:var(--text);background:var(--white);position:relative}
.abs{position:absolute}
.script{font-family:"Great Vibes",cursive;font-weight:400}
.btn{position:absolute;display:flex;align-items:center;justify-content:center;border-radius:20px;font-size:12px;font-weight:600}
.btn-white{background:var(--white);color:var(--purple)}
.btn-outline{border:2px solid var(--purple);color:var(--purple);background:var(--white)}
.btn-ghost{border:1px solid rgba(255,255,255,.35);color:var(--white)}
.btn-purple{background:var(--purple-mid);color:var(--white)}

/* header */
.site-header{top:0;left:0;width:1200px;height:75px;background:var(--white);z-index:5}
.brand-box{left:200px;top:0;width:130px;height:104px;background:var(--white);border-radius:0 0 8px 8px;box-shadow:0 4px 12px rgba(0,0,0,.08);display:flex;align-items:center;justify-content:center;z-index:6}
.brand-name{font-size:19px;font-weight:600;color:var(--purple)}
.nav{top:29px;font-size:12px;font-weight:500;color:var(--ink)}
.nav.active{color:var(--purple);font-weight:600}

/* hero */
.hero{top:75px;left:0;width:1200px;height:874px;overflow:hidden}
.hero-photo{top:0;left:0;width:1200px;height:520px;background:linear-gradient(90deg,#9a6fc0 0%,#a98bc4 40%,#8d8593 70%,#6f6a74 100%)}
.hero-title{left:200px;top:105px;font-size:38px;font-weight:700;color:var(--white);line-height:45px}
.hero-title .script{font-size:40px}
.vision-title{top:566px;left:0;width:1200px;text-align:center;color:var(--white);font-size:31px;font-weight:600}
.vision-title .script{font-size:36px}
.vision-text{top:626px;left:195px;width:810px;text-align:center;color:#e4d8ee;font-size:18px;font-weight:300;line-height:30px}

/* services */
.services{top:949px;left:0;width:1200px;height:918px;background:linear-gradient(180deg,#fff 0%,#f7f6f8 60%,#fff 100%)}
.services-bg{top:0;left:0;width:1200px;height:918px;background:radial-gradient(circle at 6% 12%,#d9d6dc 0,rgba(255,255,255,0) 180px),radial-gradient(circle at 96% 50%,#d8d6da 0,rgba(255,255,255,0) 200px)}
.section-title{left:0;width:1200px;text-align:center;font-size:31px;font-weight:700;color:var(--purple-deep)}
.section-title .script{font-size:34px;font-weight:400}
.card{position:absolute;width:388px;height:311px;background:var(--white);box-shadow:0 6px 22px rgba(60,30,90,.08);overflow:hidden;text-align:center}
.card.featured{background:var(--purple-mid);color:var(--white)}
.card-arc{position:absolute;left:124px;top:30px}
.card-title{position:absolute;top:125px;left:0;width:100%;font-size:19px;font-weight:500;color:var(--purple)}
.card.featured .card-title{color:var(--white)}
.card-text{position:absolute;top:176px;left:30px;width:328px;font-size:13px;line-height:19px;color:var(--ink)}
.card.featured .card-text{color:var(--white)}
.card-link{position:absolute;top:271px;left:0;width:100%;font-size:12px;font-weight:600;color:var(--purple)}
.card.featured .card-link{color:#e4d2f2}
.corner{position:absolute;width:0;height:0}

/* sms */
.sms-band{top:1867px;left:0;width:1200px;height:357px;background:linear-gradient(90deg,#5a2a80 0%,#613388 50%,#4f2673 100%)}
.sms-title{left:200px;top:1952px;font-size:30px;font-weight:600;color:var(--white)}
.sms-title .script{font-size:34px;font-weight:400}
.sms-text{left:200px;top:2010px;width:510px;font-size:15px;line-height:22px;color:#eadff3;font-weight:300}
.phone{left:765px;top:1808px;width:235px;height:475px;border-radius:30px;background:linear-gradient(180deg,#f6efe2 0%,#ece1cc 100%);border:7px solid #ebebee;box-shadow:0 10px 26px rgba(0,0,0,.18)}

/* why */
.why-bg{top:2224px;left:0;width:1200px;height:800px;background:linear-gradient(180deg,#ffffff 0%,#ececee 45%,#cfcdd2 100%)}
.why-text{top:2403px;left:230px;width:740px;text-align:center;font-size:15px;line-height:23px;color:var(--text);font-weight:300}
.why-text b{font-weight:600;color:var(--ink)}
.why-circle{position:absolute;border-radius:50%;background:var(--white);box-shadow:0 8px 26px rgba(60,30,90,.12);text-align:center}
.why-title{font-size:20px;font-weight:500;color:var(--purple);line-height:23px}
.why-body{font-size:13px;line-height:19px;color:var(--ink);margin-top:14px}
.why-badge{position:absolute;border-radius:50%;background:var(--purple-mid);display:flex;align-items:center;justify-content:center;box-shadow:0 0 0 5px var(--lilac-soft)}

/* newsletter */
.newsletter{top:2960px;left:0;width:1200px;height:408px;overflow:hidden}
.news-title{top:3140px;left:0;width:1200px;text-align:center;font-size:31px;font-weight:700;color:var(--white)}
.news-title .script{font-size:34px;font-weight:400}
.news-text{top:3204px;left:0;width:1200px;text-align:center;font-size:19px;color:#efe6f6;font-weight:300}
.news-text b{font-weight:700;color:var(--white)}
.news-input{left:343px;top:3253px;width:387px;height:37px;border:1px solid #e8dcf1;border-radius:20px;padding-left:24px;display:flex;align-items:center;font-size:12px;color:var(--white)}

/* footer */
.footer{top:3368px;left:0;width:1200px;height:345px;background:var(--footer)}
.f-brand{left:200px;top:3443px;width:143px;height:115px;display:flex;align-items:center;justify-content:center}
.f-brand span{font-size:22px;font-weight:600;color:var(--white)}
.f-head{top:3441px;font-size:15px;font-weight:500;color:var(--white)}
.f-item{font-size:12px;color:var(--footer-text);line-height:19px}
.f-list{font-size:11.5px;color:var(--footer-text);line-height:19px}
.social{position:absolute;top:3481px;width:30px;height:30px;border-radius:50%;background:var(--lilac)}
.social.active{background:var(--purple-mid)}
.copyright{left:200px;top:3655px;font-size:11px;color:var(--footer-text)}
.copyright b{color:var(--white);font-weight:600}
</style>
</head>
<body>

<!-- Header -->
<header class="abs site-header">
  <div class="abs brand-box"><span class="brand-name">Corvalinks</span></div>
  <span class="abs nav active" style="left:480px">~ Home ~</span>
  <span class="abs nav" style="left:555px">About</span>
  <span class="abs nav" style="left:617px">Services</span>
  <span class="abs nav" style="left:694px">SMS Product</span>
  <span class="abs nav" style="left:794px">Contact Us</span>
  <div class="btn btn-outline" style="left:887px;top:23px;width:113px;height:31px">Book A Demo</div>
</header>

<!-- Hero + Vision -->
<section class="abs hero">
  <div class="abs hero-photo" role="img" aria-label="Wooden cross draped in cloth on a rock above misty hills and a lake, tinted purple"></div>
  <svg class="abs" style="left:0;top:0" width="1200" height="874" viewBox="0 0 1200 874">
    <path d="M0 382 C230 300 420 470 690 505 C900 530 1080 470 1200 415 L1200 874 L0 874 Z" fill="var(--lilac)"/>
    <path d="M0 398 C230 320 420 490 690 520 C900 545 1080 490 1200 440 L1200 874 L0 874 Z" fill="var(--purple-deep)"/>
  </svg>
  <h1 class="abs hero-title">Your <span class="script">Trusted Partner</span> in<br>Transforming <span class="script">Communities!</span></h1>
  <div class="btn btn-white" style="left:200px;top:219px;width:113px;height:30px">Contact Us</div>
  <h2 class="abs vision-title"><span class="script">Corvalink's</span> Vision</h2>
  <p class="abs vision-text">The vision is for Corvalinks to one day become a data organization.<br>The data we will collect captures each individual church attender and participant, creates a profile for them based on the sin-to-saint spectrum model, and provides support to move individuals toward sanctification.</p>
  <div class="btn btn-ghost" style="left:537px;top:769px;width:126px;height:30px">Discover More</div>
</section>

<!-- Services -->
<section class="abs services">
  <div class="abs services-bg" role="img" aria-label="Faint rosary and praying hands in soft grey"></div>
</section>
<h2 class="abs section-title" style="top:1016px"><span class="script">Our</span> Services</h2>

<article class="card" style="left:200px;top:1089px">
  <div class="corner" style="left:0;top:0;border-top:60px solid var(--lilac);border-right:60px solid transparent"></div>
  <svg class="card-arc" width="140" height="95" viewBox="0 0 140 95"><path d="M2 93 A68 68 0 0 1 138 93" fill="none" stroke="var(--lilac)" stroke-width="2"/>
    <g fill="none" stroke="var(--purple)" stroke-width="2.5" stroke-linejoin="round"><path d="M70 18v14M64 24h12"/><path d="M52 52 L70 34 L88 52"/><rect x="55" y="50" width="30" height="27"/><path d="M66 77v-12h8v12"/><path d="M44 77h52"/></g></svg>
  <h3 class="card-title">Building Trust</h3>
  <p class="card-text">In the digital age, trust is the cornerstone of any successful organization. Corvalinks recognizes the importance of rebuilding and maintaining trust in the church ...</p>
  <span class="card-link">Read More ↗</span>
</article>

<article class="card featured" style="left:612px;top:1089px">
  <svg class="card-arc" width="140" height="95" viewBox="0 0 140 95"><path d="M2 93 A68 68 0 0 1 138 93" fill="none" stroke="#ffffff" stroke-width="2"/>
    <path d="M70 72 C45 55 45 30 58 28 C64 27 68 31 70 35 C72 31 76 27 82 28 C95 30 95 55 70 72Z" fill="none" stroke="#fff" stroke-width="2.5"/></svg>
  <h3 class="card-title">Engaging Disciples</h3>
  <p class="card-text">Unlock the potential of your community by understanding individual alignment as disciples. Corvalinks makes engagement effortless through easy-to-reply SMS surveys ...</p>
  <span class="card-link">Read More ↗</span>
</article>

<article class="card" style="left:200px;top:1426px">
  <div class="corner" style="left:0;bottom:0;border-bottom:60px solid var(--lilac);border-right:60px solid transparent"></div>
  <svg class="card-arc" width="140" height="95" viewBox="0 0 140 95"><path d="M2 93 A68 68 0 0 1 138 93" fill="none" stroke="var(--lilac)" stroke-width="2"/>
    <g fill="none" stroke="var(--purple)" stroke-width="2.5"><circle cx="70" cy="45" r="13"/><path d="M64 60h12M65 66h10M70 20v-6M50 45h-6M96 45h-6M55 30l-4-4M85 30l4-4"/></g></svg>
  <h3 class="card-title">Strategic Insights</h3>
  <p class="card-text">Corvalinks goes beyond just collecting data – we turn insights into actionable strategies. Digest survey trends to address community variance across key categories participation ...</p>
  <span class="card-link">Read More ↗</span>
</article>

<article class="card" style="left:612px;top:1426px">
  <div class="corner" style="right:0;bottom:0;border-bottom:60px solid var(--lilac);border-left:60px solid transparent"></div>
  <svg class="card-arc" width="140" height="95" viewBox="0 0 140 95"><path d="M2 93 A68 68 0 0 1 138 93" fill="none" stroke="var(--lilac)" stroke-width="2"/>
    <g fill="none" stroke="var(--purple)" stroke-width="2.5"><rect x="52" y="28" width="36" height="36" rx="6"/><path d="M52 46h36M70 28v36"/></g></svg>
  <h3 class="card-title">Unified Team Leadership</h3>
  <p class="card-text">A united team is essential for success. Corvalinks empowers your leadership with robust reporting mechanisms to share your communities insights with supporters ...</p>
  <span class="card-link">Read More ↗</span>
</article>

<!-- SMS Product -->
<section class="abs sms-band" role="img" aria-label="Church interior with pews, tinted deep purple"></section>
<h2 class="abs sms-title">SMS <span class="script">Product</span></h2>
<p class="abs sms-text">Lorem Ipsum is simply dummy text of the printing and typesetting industry. Lorem Ipsum has been the industry's standard dummy text ever since the 1500s, when an unknown printer took a galley</p>
<div class="btn btn-purple" style="left:200px;top:2102px;width:113px;height:29px">Book A Demo</div>
<div class="abs phone" role="img" aria-label="Phone showing a text-message survey conversation"></div>

<!-- Why -->
<section class="abs why-bg" role="img" aria-label="Soft grey scene of raised praying hands and flying doves"></section>
<h2 class="abs section-title" style="top:2347px">Why <span class="script">Corvalinks?</span></h2>
<p class="abs why-text">Transform your church community with Corvalinks – <b>where trust, engagement, strategy, and team leadership converge for a spiritually enriching journey.</b> Embrace the future of faith and community building with Corvalinks by your side</p>

<div class="why-circle" style="left:226px;top:2608px;width:230px;height:230px;padding:88px 26px 0">
  <div class="why-title">Tailored Solutions</div>
  <div class="why-body">Our platform is designed to meet the unique needs of religious organizations.</div>
</div>
<div class="why-circle" style="left:745px;top:2608px;width:230px;height:230px;padding:88px 26px 0">
  <div class="why-title">Trusted Partnership</div>
  <div class="why-body">Join hands with Corvalinks to build a foundation of trust and transparency.</div>
</div>
<div class="why-circle" style="left:448px;top:2556px;width:304px;height:304px;padding:112px 34px 0">
  <div class="why-title">Data-Driven<br>Spirituality</div>
  <div class="why-body">Leverage the power of data to enhance spiritual growth and community connections.</div>
</div>

<svg class="abs" style="left:0;top:2500px" width="1200" height="140" viewBox="0 0 1200 140">
  <g fill="none" stroke="var(--purple)" stroke-width="4" stroke-linecap="round">
    <path d="M341 48v46M320 66h42"/><path d="M598 0v44M577 18h42"/><path d="M860 48v46M839 66h42"/>
  </g>
</svg>
<div class="why-badge" style="left:305px;top:2597px;width:72px;height:72px">
  <svg width="28" height="28" viewBox="0 0 28 28"><rect x="5" y="5" width="18" height="18" rx="3" fill="none" stroke="#fff" stroke-width="2"/></svg></div>
<div class="why-badge" style="left:562px;top:2540px;width:72px;height:72px">
  <svg width="30" height="30" viewBox="0 0 30 30"><path d="M4 5h22v15H12l-6 5v-5H4z" fill="none" stroke="#fff" stroke-width="2"/><path d="M9 11h12M9 15h8" stroke="#fff" stroke-width="2"/></svg></div>
<div class="why-badge" style="left:824px;top:2597px;width:72px;height:72px">
  <svg width="30" height="30" viewBox="0 0 30 30"><path d="M3 14l7-6 5 4 5-4 7 6-12 9z" fill="none" stroke="#fff" stroke-width="2" stroke-linejoin="round"/></svg></div>
<div class="btn btn-outline" style="left:526px;top:2854px;width:148px;height:30px">Contact Us Today!</div>

<!-- Newsletter -->
<section class="abs newsletter">
  <svg width="1200" height="408" viewBox="0 0 1200 408" role="img" aria-label="People praying in church pews, tinted purple">
    <defs><linearGradient id="newsFill" x1="0" y1="0" x2="1" y2="1"><stop offset="0" stop-color="#5a2a80"/><stop offset="1" stop-color="#4a1f6d"/></linearGradient></defs>
    <path d="M0 76 C150 30 330 -5 520 18 C760 45 980 125 1200 110 L1200 408 L0 408 Z" fill="var(--lilac)"/>
    <path d="M0 96 C150 52 330 18 520 40 C760 68 980 145 1200 132 L1200 408 L0 408 Z" fill="url(#newsFill)"/>
  </svg>
</section>
<h2 class="abs news-title"><span class="script">Subscribe</span> Newsletter</h2>
<p class="abs news-text">To know more updates from Corvalinks LLC - <b>Subscribe Now!</b></p>
<div class="abs news-input">Enter your email ...</div>
<div class="btn btn-white" style="left:743px;top:3253px;width:113px;height:37px">Subscribe</div>

<!-- Footer -->
<footer class="abs footer"></footer>
<div class="abs f-brand"><span>Corvalinks</span></div>

<h4 class="abs f-head" style="left:387px">Contact Us</h4>
<svg class="abs" style="left:387px;top:3478px" width="14" height="14" viewBox="0 0 14 14"><path d="M3 1l3 3-2 2c1 2 2 3 4 4l2-2 3 3-2 2C6 13 1 8 1 3z" fill="#fff"/></svg>
<span class="abs f-item" style="left:410px;top:3475px;font-size:15px">123-456-7890</span>
<svg class="abs" style="left:387px;top:3512px" width="12" height="10" viewBox="0 0 12 10"><rect x="0.5" y="0.5" width="11" height="9" fill="none" stroke="#fff"/><path d="M.5 .5l5.5 5 5.5-5" fill="none" stroke="#fff"/></svg>
<span class="abs f-item" style="left:410px;top:3508px">hello@corvalinks-mail.com</span>
<svg class="abs" style="left:388px;top:3544px" width="10" height="13" viewBox="0 0 10 13"><path d="M5 13C1 8 0 6 0 5a5 5 0 0 1 10 0c0 1-1 3-5 8z" fill="#fff"/><circle cx="5" cy="5" r="1.8" fill="var(--footer)"/></svg>
<span class="abs f-item" style="left:410px;top:3541px;font-size:11.5px">Corvalinks LLC<br>418 Meadow Lane<br>Lorem Ipsum - 12345</span>

<h4 class="abs f-head" style="left:624px">Quick Links</h4>
<div class="abs f-list" style="left:624px;top:3476px">Home<br>About<br>Services<br>SMS Product<br>Contact Us</div>
<div class="abs f-list" style="left:737px;top:3476px">Term &amp; Conditions<br>Privacy Policy</div>

<h4 class="abs f-head" style="left:892px">Follow Us</h4>
<span class="social" style="left:894px" aria-label="Social profile"></span>
<span class="social active" style="left:931px" aria-label="Social profile"></span>
<span class="social" style="left:968px" aria-label="Social profile"></span>

<p class="abs copyright">© 2023 <b>Corvalinks LLC.</b> All Right Reserved</p>
<svg class="abs" style="left:1126px;top:3648px" width="16" height="18" viewBox="0 0 16 18"><path d="M8 0L16 18 8 13 0 18z" fill="var(--lilac)"/></svg>

</body>
</html>
```